New website

Our website (www.larchhollow.com) needs to be replaced with something gorgeous and glossy. We do like the text of our current website but have many new images to put on the site. We want to create a website that shows viewers what our team can do, and how we can create something amazing for them and their homes.

Coding

```html
<!DOCTYPE html>
<html lang="en">
<head>
<meta charset="utf-8">
<title>Larch Hollow Landscaping</title>
<link href="https://fonts.googleapis.com/css2?family=Fira+Sans:wght@400;500;600;700&family=Lato:wght@400;700;900&display=swap" rel="stylesheet">
<style>
:root{
  --navy:#101a47;
  --navy-deep:#0c1538;
  --green:#4cae58;
  --green-dark:#3d9a49;
  --cream:#f6f4ee;
  --mist:#e9edf3;
  --text:#4a4f5e;
  --muted:#8a8f9c;
  --white:#ffffff;
}
*{margin:0;padding:0;box-sizing:border-box}
html,body{width:1200px;height:4066px;overflow:hidden}
body{position:relative;background:var(--white);font-family:"Lato",sans-serif;color:var(--text)}
.abs{position:absolute}
.head-font{font-family:"Fira Sans",sans-serif}

/* top bar */
.topbar{left:403px;top:0;width:797px;height:33px;background:var(--navy);display:flex;align-items:center;font-size:12px;font-weight:700;color:var(--white)}
.topbar .item{display:flex;align-items:center;gap:8px;height:100%;padding:0 0 0 40px}
.topbar .appt{background:var(--green);width:268px;padding-left:34px;margin-left:40px;font-size:11px}
.topbar svg{width:15px;height:15px}
.logo{left:105px;top:22px;width:245px;text-align:center;font-family:"Fira Sans",sans-serif;font-size:26px;letter-spacing:5px;color:var(--navy);font-weight:400}
.logo small{display:block;font-size:9px;letter-spacing:9px;margin-top:2px}
.nav{left:396px;top:60px;display:flex;font-size:12px;color:var(--navy)}
.nav span{position:absolute;white-space:nowrap}
.nav .on{font-weight:700}
.btn-outline{left:932px;top:53px;width:118px;height:32px;border:1.5px solid var(--navy);border-radius:4px;font-size:12px;font-weight:700;color:var(--navy);display:flex;align-items:center;justify-content:center}

/* hero */
.hero{left:0;top:101px;width:1200px;height:673px;background:linear-gradient(90deg,#c9d4b4 0%,#9fb27e 35%,#5b7a3c 60%,#3d5a2a 85%,#2f4a22 100%)}
.hero-fade{left:0;top:101px;width:700px;height:673px;background:linear-gradient(90deg,rgba(240,240,225,.75),rgba(240,240,225,0))}
.eyebrow{left:104px;top:290px;font-family:"Fira Sans",sans-serif;font-size:20px;font-weight:600;letter-spacing:6px;color:var(--navy)}
.hero-title{left:98px;top:312px;font-family:"Fira Sans",sans-serif;font-size:72px;font-weight:600;color:var(--navy)}
.hero-copy{left:104px;top:430px;width:520px;font-size:16.5px;line-height:28px;color:#2d3247}
.btn{display:flex;align-items:center;justify-content:center;gap:12px;color:var(--white);font-weight:700;font-family:"Fira Sans",sans-serif}
.pill{height:42px;border-radius:22px;font-size:15px}
.btn-green{background:var(--green)}
.btn-navy{background:var(--navy)}

/* section labels */
.label{left:0;width:1200px;text-align:center;font-size:13px;color:var(--green-dark);font-weight:700}
.label span{display:inline-block;padding-bottom:5px;border-bottom:2px solid var(--green)}
.title{left:0;width:1200px;text-align:center;font-family:"Fira Sans",sans-serif;font-size:41px;font-weight:600;color:var(--navy)}

/* about */
.about-img{left:122px;top:977px;width:497px;height:341px;border-radius:6px;background:linear-gradient(160deg,#cfdcc4,#7fa452 50%,#4d7a2a)}
.about-card{left:568px;top:1017px;width:510px;height:281px;background:var(--cream);border-radius:6px;padding:40px 28px}
.about-card h3{font-family:"Fira Sans",sans-serif;font-size:22px;font-weight:500;color:var(--navy);margin-bottom:12px}
.about-card p{font-size:12.5px;line-height:16.5px;color:var(--muted)}
.sq{height:45px;border-radius:3px;font-size:16px}

/* services */
.services{left:0;top:1410px;width:1200px;height:578px;background:linear-gradient(180deg,#26324f,#1d2946 60%,#283551)}
.services::after{content:"";position:absolute;inset:0;background:rgba(16,26,71,.45)}
.w-label{color:var(--white)}
.w-label span{border-color:var(--white)}
.w-title{color:var(--white)}
.svc{top:1618px;width:304px;height:228px;color:var(--white)}
.svc .ph{position:absolute;inset:0}
.svc .cap{position:absolute;left:84px;top:168px}
.svc .cap h4{font-family:"Fira Sans",sans-serif;font-size:17px;font-weight:600}
.svc .cap p{font-size:13.5px;margin-top:8px}
.svc .leaf{position:absolute;left:34px;top:172px;width:30px;height:30px}
.svc.active .ov{position:absolute;inset:0;background:rgba(90,120,170,.55)}
.svc.active .txt{position:absolute;left:0;top:72px;width:100%;text-align:center;padding:0 40px}
.svc.active h4{font-family:"Fira Sans",sans-serif;font-size:17px;font-weight:600;margin-bottom:8px}
.svc.active p{font-size:13px;line-height:20px}

/* steps */
.steps{left:0;top:1988px;width:1200px;height:480px;background:var(--mist)}
.step-line{left:360px;top:2238px;width:500px;height:2px;background:var(--green)}
.step{top:2180px;width:300px;text-align:center}
.ring{width:118px;height:118px;margin:0 auto;border:2px solid var(--green);border-radius:50%;display:flex;align-items:center;justify-content:center;position:relative;background:var(--mist)}
.ring .core{width:98px;height:98px;border-radius:50%;background:var(--navy);display:flex;align-items:center;justify-content:center}
.ring .num{position:absolute;right:-12px;top:46px;width:25px;height:25px;border-radius:50%;background:var(--green);color:var(--white);font-size:10px;font-weight:700;display:flex;align-items:center;justify-content:center}
.step h4{font-family:"Fira Sans",sans-serif;font-size:18px;font-weight:600;color:var(--navy);margin-top:22px}
.step p{font-size:13.5px;line-height:20px;color:var(--muted);margin-top:4px}

/* team */
.team{left:0;top:2468px;width:1200px;height:537px;background:var(--navy-deep)}
.team-img{left:0;top:2468px;width:700px;height:537px;background:linear-gradient(90deg,#2f3d2b,#4a5a37 40%,#3a4636 65%,rgba(12,21,56,1) 100%)}
.team-label{left:632px;top:2554px;font-size:13px;font-weight:700;color:var(--green)}
.team-label span{border-bottom:2px solid var(--green);padding-bottom:4px}
.team-title{left:632px;top:2586px;font-family:"Fira Sans",sans-serif;font-size:42px;font-weight:600;line-height:53px;color:var(--white)}
.feat{left:632px;display:flex;align-items:center;gap:20px;color:var(--white)}
.feat .ic{width:63px;height:63px;border-radius:50%;background:var(--white);display:flex;align-items:center;justify-content:center}
.feat h4{font-family:"Fira Sans",sans-serif;font-size:19px;font-weight:600}
.feat p{font-size:13px;margin-top:5px}

/* testimonials */
.avatar{border-radius:50%}
.quote-mark{left:590px;top:3193px;width:60px;height:60px;border-radius:50%;background:var(--green);color:var(--white);font-family:"Fira Sans",sans-serif;font-size:46px;font-weight:700;display:flex;align-items:center;justify-content:center;line-height:1;padding-top:18px}
.review{left:330px;top:3272px;width:580px;text-align:center;font-size:15px;line-height:23px;color:var(--muted)}
.reviewer{left:0;width:1200px;text-align:center;top:3374px;font-size:13px;color:var(--text)}
.reviewer small{display:block;font-size:11px;color:var(--muted);margin-top:4px}
.arrow{top:3433px;width:44px;height:44px;border-radius:50%;background:var(--navy);display:flex;align-items:center;justify-content:center}

/* footer */
.footer{left:0;top:3560px;width:1200px;height:506px}
.f-logo{left:0;top:3738px;width:1200px;text-align:center;font-family:"Fira Sans",sans-serif;font-size:32px;letter-spacing:7px;color:#59627f}
.f-logo small{display:block;font-size:10px;letter-spacing:11px;margin-top:2px}
.f-nav{top:3829px;font-size:14px;font-weight:700;color:var(--white);white-space:nowrap}
.f-rule{left:140px;top:3878px;width:918px;height:1px;background:#6a7290}
.f-contact{top:3923px;display:flex;align-items:center;gap:14px;color:var(--white);font-size:12px;font-weight:700;line-height:18px}
.f-contact .ic{width:56px;height:56px;border-radius:50%;border:1.5px solid var(--white);display:flex;align-items:center;justify-content:center}
.f-contact b{font-size:15px;font-weight:700}
.f-div{top:3925px;width:1.5px;height:60px;background:var(--white)}
.bottom{left:0;top:4012px;width:1200px;height:54px;background:var(--green)}
.bottom .name{position:absolute;left:147px;top:18px;color:var(--white);font-size:13px;font-weight:700}
.social{position:absolute;top:14px;width:26px;height:26px;border:1.5px solid var(--white);border-radius:3px}
</style>
</head>
<body>

<!-- Header -->
<div class="abs topbar">
  <div class="item"><svg viewBox="0 0 24 24" fill="none" stroke="#fff" stroke-width="2"><path d="M5 3h4l2 5-3 2a12 12 0 0 0 6 6l2-3 5 2v4a2 2 0 0 1-2 2A17 17 0 0 1 3 5a2 2 0 0 1 2-2z"/></svg>512 - 555 - 0148</div>
  <div class="item appt"><svg viewBox="0 0 24 24" fill="none" stroke="#fff" stroke-width="2"><rect x="3" y="5" width="18" height="14" rx="1"/><path d="M3 6l9 7 9-7"/></svg>REQUEST AN APPOINTMENT</div>
  <div class="item" style="padding-left:24px"><svg viewBox="0 0 24 24" fill="none" stroke="#fff" stroke-width="2"><path d="M12 22s7-7 7-12a7 7 0 0 0-14 0c0 5 7 12 7 12z"/><circle cx="12" cy="10" r="2.5"/></svg>1234 Some PLace Somewhere</div>
</div>
<div class="abs logo">LARCH HOLLOW<small>LANDSCAPING</small></div>
<div class="abs nav">
  <span class="on" style="left:0">Home</span>
  <span style="left:74px">About Us</span>
  <span style="left:150px">Services</span>
  <span style="left:226px">Our Team</span>
  <span style="left:311px">Contact Us</span>
</div>
<div class="abs btn-outline">CONTACT US</div>

<!-- Hero -->
<div class="abs hero" role="img" aria-label="Gardener in work overalls pushing a lawn mower across a green garden"></div>
<div class="abs hero-fade"></div>
<svg class="abs" style="left:0;top:680px" width="1200" height="100" viewBox="0 0 1200 100" preserveAspectRatio="none">
  <path d="M0 50 C250 0 520 10 760 50 S1100 70 1200 30 L1200 100 L0 100Z" fill="#4cae58"/>
  <path d="M0 58 C250 8 520 20 760 62 S1100 80 1200 45 L1200 100 L0 100Z" fill="#fff"/>
</svg>
<div class="abs eyebrow">EXPERTS IN</div>
<div class="abs hero-title">Landscaping</div>
<div class="abs hero-copy">Lorem ipsum dolor sit amet, consectetur adipiscing elit, sed do ei usmod tempor incididunt ut lab</div>
<div class="abs btn btn-green pill" style="left:104px;top:515px;width:146px">LEARN MORE</div>
<div class="abs btn btn-navy pill" style="left:259px;top:515px;width:183px">REQUEST QUOTE</div>

<!-- About -->
<div class="abs label" style="top:846px"><span>ABOUT US</span></div>
<div class="abs title" style="top:883px">Who We Are</div>
<div class="abs about-img" role="img" aria-label="Landscaper trimming a hedge with a power trimmer beside a garden path"></div>
<div class="abs about-card">
  <h3>Cultivating Beauty Outdoors</h3>
  <p>Lorem ipsum dolor sit amet, consectetur adipiscing elit, sed do eiusmod tempor incididunt ut labore et dolore magna aliqua. Ut enim ad minim veniam, quis nostrud exercitation ullamco laboris nisi ut aliquip ex ea commodo consequat. Duis aute irure dolor in reprehenderit in voluptate velit esse cillum dolore eu fugiat nulla pariatur. Excepteur sint occaecat cupidatat</p>
</div>
<div class="abs btn btn-green sq" style="left:595px;top:1220px;width:157px">Contact us
  <svg width="18" height="14" viewBox="0 0 18 14" fill="none" stroke="#fff" stroke-width="2"><path d="M1 7h15M10 1l6 6-6 6"/></svg></div>

<!-- Services -->
<div class="abs services" role="img" aria-label="Dusk view of a house front with garage and driveway"></div>
<div class="abs label w-label" style="top:1488px"><span>OUR SERVICES</span></div>
<div class="abs title w-title" style="top:1523px">Services We Offer</div>

<div class="abs svc active" style="left:140px">
  <div class="ph" role="img" aria-label="Designer discussing a garden plan with a client" style="background:linear-gradient(135deg,#6d8c9c,#4f6f7e)"></div>
  <div class="ov"></div>
  <div class="txt"><h4>Landscape Design</h4><p>Lorem ipsum dolor sit amet, con sectetur adipiscing elit, sed do eiusmod tempor</p>
    <svg width="28" height="14" viewBox="0 0 28 14" fill="none" stroke="#fff" stroke-width="1.5" style="margin-top:10px"><path d="M1 7h25M20 1l6 6-6 6"/></svg></div>
</div>
<div class="abs svc" style="left:467px">
  <div class="ph" role="img" aria-label="Gardener pruning a bonsai-shaped shrub" style="background:linear-gradient(180deg,#5f7d4a,#3b4e35 60%,#2a3324)"></div>
  <svg class="leaf" viewBox="0 0 30 30" fill="none" stroke="#4cae58" stroke-width="2"><path d="M4 26h22M8 22c0-8 6-14 14-16-1 8-6 14-14 16z"/><path d="M8 22l8-9"/></svg>
  <div class="cap"><h4>Irrigation Systems</h4><p>Lorem ipsum dolor sit amet</p></div>
</div>
<div class="abs svc" style="left:794px">
  <div class="ph" role="img" aria-label="Hands planting a young green shrub" style="background:linear-gradient(180deg,#6e8f45,#3c5230 60%,#252d22)"></div>
  <svg class="leaf" viewBox="0 0 30 30" fill="none" stroke="#4cae58" stroke-width="2"><path d="M4 26h22M8 22c0-8 6-14 14-16-1 8-6 14-14 16z"/><path d="M8 22l8-9"/></svg>
  <div class="cap"><h4>Outdoor Lighting</h4><p>Lorem ipsum dolor sit amet</p></div>
</div>
<div class="abs btn btn-green sq" style="left:542px;top:1893px;width:154px;z-index:2">Contact us
  <svg width="18" height="14" viewBox="0 0 18 14" fill="none" stroke="#fff" stroke-width="2"><path d="M1 7h15M10 1l6 6-6 6"/></svg></div>

<!-- Steps -->
<div class="abs steps"></div>
<div class="abs label" style="top:2045px"><span>STEPS</span></div>
<div class="abs title" style="top:2081px">Simple Steps</div>
<div class="abs step-line"></div>
<div class="abs step" style="left:150px">
  <div class="ring"><div class="core"><svg width="40" height="40" viewBox="0 0 30 30" fill="none" stroke="#fff" stroke-width="1.6"><path d="M4 26h22M8 22c0-8 6-14 14-16-1 8-6 14-14 16z"/><path d="M8 22l8-9"/></svg></div><div class="num">01</div></div>
  <h4>Contact Us to Start</h4><p>Lorem ipsum dolor sit amet,<br>consectetur adipiscing elit,<br>sed do eiusmod</p>
</div>
<div class="abs step" style="left:466px">
  <div class="ring"><div class="core"><svg width="40" height="40" viewBox="0 0 30 30" fill="none" stroke="#fff" stroke-width="1.6"><path d="M4 26h22M8 22c0-8 6-14 14-16-1 8-6 14-14 16z"/><path d="M8 22l8-9"/></svg></div><div class="num">01</div></div>
  <h4>Set Up an Appointment</h4><p>Lorem ipsum dolor sit amet,<br>consectetur adipiscing elit,<br>sed do eiusmod</p>
</div>
<div class="abs step" style="left:782px">
  <div class="ring"><div class="core"><svg width="40" height="40" viewBox="0 0 30 30" fill="none" stroke="#fff" stroke-width="1.6"><path d="M4 26h22M8 22c0-8 6-14 14-16-1 8-6 14-14 16z"/><path d="M8 22l8-9"/></svg></div><div class="num">01</div></div>
  <h4>Get Assigned an Expert</h4><p>Lorem ipsum dolor sit amet,<br>consectetur adipiscing elit,<br>sed do eiusmod</p>
</div>

<!-- Team -->
<div class="abs team"></div>
<div class="abs team-img" role="img" aria-label="Landscaper in an apron writing on a clipboard in an evening-lit garden"></div>
<div class="abs team-label"><span>WHO WE ARE</span></div>
<div class="abs team-title">The team you can trust<br>to get the job done</div>
<div class="abs feat" style="top:2718px">
  <div class="ic"><svg width="34" height="34" viewBox="0 0 24 24" fill="none" stroke="#4cae58" stroke-width="1.6"><path d="M12 3l2.6 5.3 5.9.9-4.3 4.1 1 5.8L12 16.4 6.8 19.1l1-5.8L3.5 9.2l5.9-.9z"/></svg></div>
  <div><h4>On-Time Appointments</h4><p>Lorem ipsum dolor sit amet, consectetur sipid</p></div>
</div>
<div class="abs feat" style="top:2802px">
  <div class="ic"><svg width="34" height="34" viewBox="0 0 24 24" fill="none" stroke="#4cae58" stroke-width="1.6"><path d="M12 3l2.6 5.3 5.9.9-4.3 4.1 1 5.8L12 16.4 6.8 19.1l1-5.8L3.5 9.2l5.9-.9z"/></svg></div>
  <div><h4>Client Centric</h4><p>Lorem ipsum dolor sit amet, consectetur sipid</p></div>
</div>
<div class="abs feat" style="top:2885px">
  <div class="ic"><svg width="34" height="34" viewBox="0 0 24 24" fill="none" stroke="#4cae58" stroke-width="1.6"><path d="M12 3l2.6 5.3 5.9.9-4.3 4.1 1 5.8L12 16.4 6.8 19.1l1-5.8L3.5 9.2l5.9-.9z"/></svg></div>
  <div><h4>Experienced Professionals</h4><p>Lorem ipsum dolor sit amet, consectetur sipid</p></div>
</div>

<!-- Testimonials -->
<div class="abs label" style="top:3061px"><span>TESTIMONIALS</span></div>
<div class="abs title" style="top:3097px">Client Reviews</div>
<div class="abs avatar" role="img" aria-label="Client portrait" style="left:242px;top:3193px;width:60px;height:60px;background:#e4dcd6"></div>
<div class="abs avatar" role="img" aria-label="Client portrait" style="left:91px;top:3250px;width:100px;height:100px;background:#a88466"></div>
<div class="abs avatar" role="img" aria-label="Client portrait" style="left:261px;top:3310px;width:40px;height:40px;background:#d6d2cf"></div>
<div class="abs avatar" role="img" aria-label="Client portrait" style="left:171px;top:3385px;width:84px;height:84px;background:#e7ddd6"></div>
<div class="abs avatar" role="img" aria-label="Client portrait" style="left:892px;top:3179px;width:50px;height:50px;background:#9a9a9c"></div>
<div class="abs avatar" role="img" aria-label="Client portrait" style="left:1003px;top:3237px;width:104px;height:104px;background:#d9d9dc"></div>
<div class="abs avatar" role="img" aria-label="Client portrait" style="left:871px;top:3351px;width:62px;height:62px;background:#f2c98c"></div>
<div class="abs avatar" role="img" aria-label="Client portrait" style="left:996px;top:3388px;width:82px;height:82px;background:#eeeae3"></div>
<div class="abs quote-mark">”</div>
<div class="abs review">Lorem ipsum dolor sit amet, consectetur adipiscing elit, sed do eiusmod tempor incididunt ut labore et dolore magna aliqua. Ut enim ad minim veniam, quis nostrud exercitation ullamco laboris nisi ut aliquip ex ea comm odo consequat. Duis aute irure</div>
<div class="abs reviewer">Marcus Bell<small>Client</small></div>
<div class="abs arrow" style="left:569px"><svg width="12" height="14" viewBox="0 0 12 14" fill="none" stroke="#fff" stroke-width="2"><path d="M3 1l6 6-6 6"/></svg></div>
<div class="abs arrow" style="left:624px"><svg width="12" height="14" viewBox="0 0 12 14" fill="none" stroke="#fff" stroke-width="2"><path d="M9 1L3 7l6 6"/></svg></div>

<!-- Footer -->
<svg class="abs footer" viewBox="0 0 1200 506" preserveAspectRatio="none">
  <path d="M0 40 C300 -10 500 20 760 40 S1100 60 1200 40 L1200 506 L0 506Z" fill="#4cae58"/>
  <path d="M0 80 C300 20 520 40 760 60 S1100 75 1200 60 L1200 506 L0 506Z" fill="#0c1538"/>
</svg>
<div class="abs f-logo">LARCH HOLLOW<small>LANDSCAPING</small></div>
<div class="abs f-nav" style="left:352px">HOME</div>
<div class="abs f-nav" style="left:445px">SERVICES</div>
<div class="abs f-nav" style="left:550px">ABOUT US</div>
<div class="abs f-nav" style="left:670px">TESTIMONIALS</div>
<div class="abs f-nav" style="left:821px">BLOG</div>
<div class="abs f-rule"></div>
<div class="abs f-contact" style="left:172px">
  <div class="ic"><svg width="30" height="30" viewBox="0 0 24 24" fill="none" stroke="#fff" stroke-width="1.3"><circle cx="12" cy="12" r="9"/><path d="M3 12h18M12 3c3 3 3 15 0 18M12 3c-3 3-3 15 0 18"/></svg></div>
  <div>123, Building Name, Street<br>City, State XY 123456</div>
</div>
<div class="abs f-div" style="left:429px"></div>
<div class="abs f-contact" style="left:506px">
  <div class="ic"><svg width="28" height="28" viewBox="0 0 24 24" fill="none" stroke="#fff" stroke-width="1.3"><rect x="7" y="3" width="10" height="18" rx="1.5"/><path d="M11 18h2"/></svg></div>
  <div><b>PHONE</b><br>(123) 456 7890</div>
</div>
<div class="abs f-div" style="left:750px"></div>
<div class="abs f-contact" style="left:828px">
  <div class="ic"><svg width="28" height="28" viewBox="0 0 24 24" fill="none" stroke="#fff" stroke-width="1.3"><rect x="3" y="6" width="18" height="13" rx="1"/><path d="M3 7l9 7 9-7"/></svg></div>
  <div><b>EMAIL</b><br>info@company.com</div>
</div>
<div class="abs bottom">
  <div class="name">Larch Hollow</div>
  <div class="social" style="left:946px"></div>
  <div class="social" style="left:978px"></div>
  <div class="social" style="left:1010px"></div>
  <div class="social" style="left:1042px"></div>
</div>

</body>
</html>
```